Dental Office Needs- Flyer Design for Same Day Crowns

We need a flyer that will explain the benefits of the same day crown from the patient prospective. Not show pictures of the machine that makes the crowns. See attached material for content. The flyer should use the practices PMS colors of Green 562 and Blue 3025. The ad should say to the patient - I want to go this office and get my crown done there.
Updates

Project Deadline Extended Reason: The difference in the time zone between USA and Europe has caused issues. Minor changes still need to be worked out. Added Thursday, July 14, 2016

Target Market(s)

Dental Patients

Industry/Entity Type

Dental

Requirements
Must have
• Call to Action
• Business Address and Business Logo
• Classic Design
• images of a Happy 50 year old Couple
• Gives the benefits of the same day crown
Should not have
• No Images of tooth figures
• No before or after pictures

```html
<!DOCTYPE html>
<html lang="en">
<head>
<meta charset="utf-8">
<title>Brookfield Dental Care – Same-Day Crowns</title>
<link href="https://fonts.googleapis.com/css2?family=Cinzel:wght@400;700&family=Jost:wght@400;500&family=Montserrat:wght@400&family=Great+Vibes&display=swap" rel="stylesheet">
<style>
  :root{
    --green:#0a8775;
    --teal-panel:#088a78;
    --blue:#0b5a8a;
    --white:#ffffff;
    --photo-light:#eef1e4;
    --photo-mid:#c9d8a8;
    --photo-sky:#dfeaf0;
  }
  *{margin:0;padding:0;box-sizing:border-box}
  html,body{width:1200px;height:927px;overflow:hidden;background:var(--white)}
  .flyer{position:relative;width:1200px;height:927px;background:var(--white);font-family:"Jost",sans-serif}

  /* Left panel */
  .benefits{position:absolute;left:0;top:0;width:401px;height:927px}
  .benefits-title{position:absolute;left:41px;top:42px;font-family:"Cinzel",serif;font-weight:700;font-size:64px;line-height:1;color:var(--blue);letter-spacing:1px;white-space:nowrap}
  .benefits-sub{position:absolute;left:41px;top:108px;font-family:"Cinzel",serif;font-weight:700;font-size:22px;color:var(--green);white-space:nowrap}
  .benefit-list{list-style:none;position:absolute;left:40px;top:0;width:340px}
  .benefit-list li{position:absolute;left:0;width:340px;padding-left:39px;font-weight:500;font-size:21.5px;line-height:27px;color:var(--blue)}
  .benefit-list svg{position:absolute;left:0;top:4px;width:26px;height:26px}
  .couple-bike{position:absolute;left:0;top:692px;width:401px;height:235px;background:linear-gradient(180deg,var(--white) 0%,#cfe0b4 25%,#9fbf73 70%,#86a85a 100%)}

  /* Middle panel */
  .intro{position:absolute;left:401px;top:0;width:397px;height:927px;background:var(--teal-panel);color:var(--white)}
  .intro-kicker{position:absolute;left:37px;top:52px;font-family:"Cinzel",serif;font-weight:700;font-size:16.4px;white-space:nowrap}
  .intro-title{position:absolute;left:37px;top:70px;font-family:"Cinzel",serif;font-weight:700;font-size:31.4px;white-space:nowrap}
  .body-copy{position:absolute;left:37px;width:324px;font-family:"Montserrat",sans-serif;font-size:14.2px;line-height:20px;text-align:justify;hyphens:auto;-webkit-hyphens:auto}
  .body-copy p+p{margin-top:20px}
  .how-band{position:absolute;left:0;top:550px;width:397px;height:58px;background:var(--blue);display:flex;align-items:center;padding-left:37px;font-family:"Cinzel",serif;font-weight:700;font-size:15.5px}

  /* Right panel */
  .cover{position:absolute;left:798px;top:0;width:402px;height:927px}
  .cover-photo{position:absolute;left:0;top:220px;width:402px;height:707px;background:linear-gradient(180deg,var(--white) 0%,var(--photo-sky) 12%,var(--photo-light) 45%,var(--photo-mid) 100%)}
  .brand{position:absolute;left:0;top:58px;width:402px;text-align:center;color:var(--green)}
  .brand-mark{display:block;width:34px;height:34px;margin:0 auto 22px;border-radius:50%;background:var(--green)}
  .brand-name{font-family:"Jost",sans-serif;font-weight:400;font-size:30px;line-height:1}
  .brand-tag{font-family:"Great Vibes",cursive;font-size:22px;margin-top:8px}
  .headline{position:absolute;left:0;width:402px;text-align:center;font-family:"Cinzel",serif;font-weight:700;line-height:1;white-space:nowrap}
  .hl-ask{top:512px;font-size:21px;color:var(--green)}
  .hl-healthy{top:530px;font-size:49px;color:var(--green)}
  .hl-beautiful{top:577px;font-size:51px;color:var(--green)}
  .hl-smile{top:615px;font-size:98px;color:var(--green)}
  .hl-injust{top:702px;font-size:21px;color:var(--blue)}
  .hl-one{top:712px;font-size:131px;color:var(--blue)}
  .hl-visit{top:829px;font-size:41px;color:var(--green)}
</style>
</head>
<body>
<main class="flyer">

  <section class="benefits">
    <h1 class="benefits-title">BENEFITS</h1>
    <p class="benefits-sub">OF THE SAME-DAY CROWNS</p>
    <ul class="benefit-list">
      <li style="top:154px"><svg viewBox="0 0 26 26"><path d="M2 14 L9 22 L24 3" fill="none" stroke="var(--green)" stroke-width="4" stroke-linecap="round" stroke-linejoin="round"/></svg>A beautiful, new smile<br>in a single visit</li>
      <li style="top:226px"><svg viewBox="0 0 26 26"><path d="M2 14 L9 22 L24 3" fill="none" stroke="var(--green)" stroke-width="4" stroke-linecap="round" stroke-linejoin="round"/></svg>Saves you valuable time</li>
      <li style="top:275px"><svg viewBox="0 0 26 26"><path d="M2 14 L9 22 L24 3" fill="none" stroke="var(--green)" stroke-width="4" stroke-linecap="round" stroke-linejoin="round"/></svg>No more unpleasant<br>temporary crowns</li>
      <li style="top:346px"><svg viewBox="0 0 26 26"><path d="M2 14 L9 22 L24 3" fill="none" stroke="var(--green)" stroke-width="4" stroke-linecap="round" stroke-linejoin="round"/></svg>Noninvasive procedure</li>
      <li style="top:396px"><svg viewBox="0 0 26 26"><path d="M2 14 L9 22 L24 3" fill="none" stroke="var(--green)" stroke-width="4" stroke-linecap="round" stroke-linejoin="round"/></svg>No need for impressions<br>and no more discomfort</li>
      <li style="top:462px"><svg viewBox="0 0 26 26"><path d="M2 14 L9 22 L24 3" fill="none" stroke="var(--green)" stroke-width="4" stroke-linecap="round" stroke-linejoin="round"/></svg>Same-day color corrections</li>
      <li style="top:512px"><svg viewBox="0 0 26 26"><path d="M2 14 L9 22 L24 3" fill="none" stroke="var(--green)" stroke-width="4" stroke-linecap="round" stroke-linejoin="round"/></svg>Less prone to cracks and<br>flaws than other types of<br>restoration</li>
      <li style="top:605px"><svg viewBox="0 0 26 26"><path d="M2 14 L9 22 L24 3" fill="none" stroke="var(--green)" stroke-width="4" stroke-linecap="round" stroke-linejoin="round"/></svg>Increased accuracy, result-<br>ing in a perfect, personal-<br>ized fit</li>
    </ul>
    <div class="couple-bike" role="img" aria-label="Photo of a smiling senior couple riding bicycles outdoors"></div>
  </section>

  <section class="intro">
    <p class="intro-kicker">INTRODUCING THE REVOLUTIONARY</p>
    <h2 class="intro-title">SAME-DAY CROWNS</h2>
    <div class="body-copy" style="top:118px">
      <p>Same-day crowns use cutting-edge CAD/CAM technology - such as SMILEFORGE® technology - to build a permanent, custom-fit, natural-looking, metal-free restoration that provides the form, fit, and function you need.</p>
      <p>Traditional crowns entail multiple visits and the inconvenience of temporaries while waiting for the crown to be made and fit properly. They often do not look natural and can even cause pain if they are not fitted properly.</p>
      <p>Using the advanced SAME-DAY CROWN TECHNOLOGY, we design and generate porcelain crowns in just one visit, providing you with a faster, more esthetic result, less injections and drilling, and no temporary crowns or goopy impressions.</p>
    </div>
    <h3 class="how-band">HOW DO SAME-DAY CROWNS WORK?</h3>
    <div class="body-copy" style="top:625px">
      <p>We begin the process by using a laser wand to quickly, safely, and accurately create a digital, 3-D model of the tooth in need of repair. The crown is then immediately designed in the office using the CAD/CAM software.</p>
      <p>Once the design is finished, the new tooth is created in an on-site milling center right in front of your eyes. We will then cement it into place, and you are good to go home with a healthy, gorgeous smile again!</p>
    </div>
  </section>

  <section class="cover">
    <div class="cover-photo" role="img" aria-label="Faded photo of a happy senior couple embracing in a sunny meadow"></div>
    <div class="brand">
      <span class="brand-mark"></span>
      <p class="brand-name">Brookfield Dental Care</p>
      <p class="brand-tag">It All Begins With a Healthy Smile!</p>
    </div>
    <p class="headline hl-ask">WOULD YOU LIKE TO HAVE</p>
    <p class="headline hl-healthy">A HEALTHY,</p>
    <p class="headline hl-beautiful">BEAUTIFUL</p>
    <p class="headline hl-smile">SMILE</p>
    <p class="headline hl-injust">IN JUST</p>
    <p class="headline hl-one">ONE</p>
    <p class="headline hl-visit">OFFICE VISIT?</p>
  </section>

</main>
</body>
</html>
```